rk ironcraft business card metallic look

revamp the existing design but want card to have a metalic look to it

Target Market(s)

construction industry

Industry/Entity Type

constrction

Contact Information for Business Card

front of card RK Ironcraft, phone 4165550193, email rk.ironcraftt@veltrano.com and instagram account; rk_ironcraft_

Font styles to use
Other font styles liked:
• masculine

Colors

Designer to choose only greyscale colors for use in the design.

Requirements
Must have
• back side RK Ironcraft then a list of everything : Siding, ACM Panels, Standing Seam,Soffit, Fascia, Gutters,Metal,Alu,inum, Viynyl, Metal Roofs and roof repairs
Nice to have
• I would like to keep the look of the existing card with the metal grids on the front
Should not have
• Need a design in two days

```html
<!DOCTYPE html>
<html lang="en">
<head>
<meta charset="utf-8">
<title>RK Ironcraft – Business Card</title>
<link rel="stylesheet" href="https://fonts.googleapis.com/css2?family=Oswald:wght@600&family=Roboto:wght@500&family=Exo+2:wght@600&display=swap">
<style>
  :root {
    --page: #ffffff;
    --steel-dark: #101010;
    --steel-mid: #4d4d4d;
    --band: #0d0c0b;
    --chrome: #d6d6d6;
    --contact: #f2f2f2;
    --ink: #1b1b1f;
    --service: #c9c5bd;
    --back-dark: #181818;
  }
  * { margin: 0; padding: 0; box-sizing: border-box; }
  html, body { width: 1200px; height: 1200px; overflow: hidden; background: var(--page); }
  .sheet { position: relative; width: 1200px; height: 1200px; }
  .card { position: absolute; left: 229px; width: 749px; height: 429px; overflow: hidden; }
  .card--front { top: 127px; }
  .card--back { top: 652px; height: 428px; }
  .card-art { position: absolute; inset: 0; width: 100%; height: 100%; }

  .wordmark {
    position: absolute; left: 0; right: 0; text-align: center;
    font-family: "Oswald", sans-serif; font-weight: 600; line-height: 1;
  }
  .wordmark__initials { display: block; font-size: 96px; letter-spacing: 2px; }
  .wordmark__name { display: block; font-size: 44px; letter-spacing: 3px; margin-top: 4px; }
  .card--front .wordmark { top: 118px; color: var(--chrome); }
  .card--back .wordmark { top: 100px; color: var(--ink); }
  .card--back .wordmark__initials { font-size: 72px; }
  .card--back .wordmark__name { font-size: 36px; letter-spacing: 1px; }

  .contact-row {
    position: absolute; left: 0; right: 0; top: 354px; height: 75px;
    font-family: "Roboto", sans-serif; font-weight: 500; font-size: 16px; color: var(--contact);
  }
  .contact { position: absolute; top: 27px; display: flex; align-items: center; gap: 10px; white-space: nowrap; }
  .contact--phone { left: 45px; }
  .contact--email { left: 240px; }
  .contact--social { left: 535px; }
  .contact svg { flex: none; }

  .services {
    position: absolute; left: 0; right: 0; top: 326px; text-align: center;
    font-family: "Exo 2", sans-serif; font-weight: 600; font-size: 19px; line-height: 24px;
    letter-spacing: 1px; color: var(--service);
  }
</style>
</head>
<body>
<main class="sheet">

  <section class="card card--front" aria-label="Business card front">
    <svg class="card-art" viewBox="0 0 749 429" aria-hidden="true">
      <defs>
        <linearGradient id="brushed" x1="0" y1="0" x2="0" y2="1">
          <stop offset="0" stop-color="#0e0e0e"/>
          <stop offset="0.35" stop-color="#555555"/>
          <stop offset="0.55" stop-color="#3a3a3a"/>
          <stop offset="0.85" stop-color="#141414"/>
        </linearGradient>
        <linearGradient id="plateLeft" x1="0" y1="0" x2="1" y2="0">
          <stop offset="0" stop-color="#8a8a87"/>
          <stop offset="1" stop-color="#4a4a4a"/>
        </linearGradient>
        <linearGradient id="plateRight" x1="0" y1="0" x2="1" y2="0">
          <stop offset="0" stop-color="#8a8a8a"/>
          <stop offset="1" stop-color="#3c3c3c"/>
        </linearGradient>
      </defs>
      <rect width="749" height="429" fill="url(#brushed)"/>
      <polygon points="0,0 156,0 0,111" fill="url(#plateLeft)"/>
      <line x1="156" y1="0" x2="0" y2="111" stroke="#9a9a9a" stroke-width="3"/>
      <polygon points="627,0 749,0 749,98 725,120 592,25" fill="url(#plateRight)" stroke="#a0a0a0" stroke-width="3"/>
      <line x1="749" y1="145" x2="671" y2="193" stroke="#8c8c8c" stroke-width="1.5"/>
      <line x1="749" y1="170" x2="602" y2="257" stroke="#9a9a9a" stroke-width="2"/>
      <rect y="354" width="749" height="75" fill="var(--band)"/>
    </svg>

    <div class="wordmark">
      <span class="wordmark__initials">RK</span>
      <span class="wordmark__name">IRONCRAFT</span>
    </div>

    <div class="contact-row">
      <span class="contact contact--phone">
        <svg width="19" height="19" viewBox="0 0 20 20"><circle cx="10" cy="10" r="10" fill="#e8e8e8"/><path d="M6.5 5.2l2 0 .8 2.6-1.2 1a7 7 0 0 0 3.2 3.2l1-1.2 2.6.8v2c0 .6-.5 1-1 1A9 9 0 0 1 5.5 6.2c0-.6.4-1 1-1z" fill="#0d0c0b"/></svg>
        416-555-0193
      </span>
      <span class="contact contact--email">
        <svg width="24" height="16" viewBox="0 0 24 16"><rect x="1" y="1" width="22" height="14" fill="none" stroke="#e8e8e8" stroke-width="2"/><path d="M1 1l11 8 11-8M1 15l8-7M23 15l-8-7" fill="none" stroke="#e8e8e8" stroke-width="1.6"/></svg>
        rk.ironcraftt@veltrano.com
      </span>
      <span class="contact contact--social">
        <svg width="18" height="18" viewBox="0 0 18 18"><rect width="18" height="18" rx="3" fill="#e8e8e8"/></svg>
        rk_ironcraft_
      </span>
    </div>
  </section>

  <section class="card card--back" aria-label="Business card back">
    <svg class="card-art" viewBox="0 0 749 428" aria-hidden="true">
      <defs>
        <linearGradient id="sheen" x1="0" y1="0" x2="1" y2="0">
          <stop offset="0" stop-color="#474645"/>
          <stop offset="0.45" stop-color="#8a8a8a"/>
          <stop offset="0.8" stop-color="#c4c4c4"/>
          <stop offset="1" stop-color="#d2d2d2"/>
        </linearGradient>
      </defs>
      <rect width="749" height="428" fill="url(#sheen)"/>
      <line x1="0" y1="82" x2="80" y2="129" stroke="#7a7a7a" stroke-width="1.5"/>
      <line x1="0" y1="106" x2="149" y2="195" stroke="#8e8e8e" stroke-width="2"/>
      <line x1="749" y1="82" x2="669" y2="129" stroke="#9c9c9c" stroke-width="1.5"/>
      <line x1="749" y1="106" x2="600" y2="195" stroke="#a6a6a6" stroke-width="2"/>
      <polygon points="0,314 374,232 374,248 0,330" fill="#4a4a4a"/>
      <polygon points="374,232 749,310 749,330 374,248" fill="#cfcfcf"/>
      <polygon points="0,330 374,248 749,330 749,428 0,428" fill="var(--back-dark)"/>
    </svg>

    <div class="wordmark">
      <span class="wordmark__initials">RK</span>
      <span class="wordmark__name">IRONCRAFT</span>
    </div>

    <p class="services">
      Siding, ACM Panels, Standing Seam,<br>
      Soffit, Fascia, Gutters, Metal, Alumunium, Viynyl,<br>
      Metal Roofs and roof repairs
    </p>
  </section>

</main>
</body>
</html>
```